Summit Grading a Masonry LLC business card

My current business card is very plain. it has my logo and contact information. I woud like something that stands out from the rest. please take a look at my website to see about my company.

Compayt Name - Summit Grading And Masonry
Owner - Martin Galloway
Business Address
Business Website - www.summitgradingandmasonry.example
Email - Summitgradingandmasonry@mailbox.example
Phone - 555-214-3867
Fax - 555-630-2719

Target Market(s)

Everyone age tang is 18 - 85

Industry/Entity Type

Business

Contact Information for Business Card

Nice and professional all in one.

Font styles to use
Serif
Other font styles liked:
• Up to you

Requirements
Must have
• All contact info. The design is up to you.
Nice to have
• All the contact info the design is up to you
Should not have
• I don't have any

```html
<!DOCTYPE html>
<html lang="en">
<head>
<meta charset="UTF-8">
<title>Summit Grading &amp; Masonry LLC – Business Card</title>
<link rel="stylesheet" href="https://fonts.googleapis.com/css2?family=Old+Standard+TT:wght@400&family=Open+Sans:wght@400;700&display=swap">
<style>
  :root {
    --backdrop: #1b1b1c;
    --card: #2d2d2e;
    --card-edge: #353536;
    --seal: #3a3a3b;
    --mark-text: #c9c9c9;
    --accent: #f7941d;
    --text-light: #e6e6e6;
    --text-muted: #bdbdbd;
    --badge: #8a8a8a;
  }
  * { margin: 0; padding: 0; box-sizing: border-box; }
  html, body {
    width: 1200px;
    height: 1000px;
    overflow: hidden;
    background: var(--backdrop);
  }
  .stage { position: relative; width: 1200px; height: 1000px; }

  .card {
    position: absolute;
    width: 520px;
    height: 300px;
    border-radius: 22px;
    background: var(--card);
    overflow: hidden;
    box-shadow: 0 12px 30px rgba(0,0,0,0.45);
  }

  /* Front */
  .card-front { left: 90px; top: 150px; }
  .front-seal {
    position: absolute;
    left: 50%; top: 50%;
    width: 230px; height: 230px;
    margin: -115px 0 0 -115px;
    border-radius: 50%;
    background: var(--seal);
  }
  .front-name {
    position: absolute;
    left: 0; right: 0; top: 50%;
    transform: translateY(-50%);
    text-align: center;
    font-family: "Old Standard TT", serif;
    font-weight: 400;
    font-size: 38px;
    line-height: 1.05;
    letter-spacing: 0.5px;
    color: var(--mark-text);
  }

  /* Back */
  .card-back { left: 590px; top: 540px; }
  .back-mark {
    position: absolute;
    right: 26px; top: 70px;
    font-family: "Old Standard TT", serif;
    font-weight: 400;
    font-size: 15px;
    line-height: 1.05;
    color: var(--text-light);
    text-align: left;
  }
  .owner-name {
    position: absolute;
    left: 36px; top: 52px;
    font-family: "Open Sans", sans-serif;
    font-weight: 700;
    font-size: 24px;
    color: var(--accent);
    letter-spacing: 0.2px;
  }
  .owner-title {
    position: absolute;
    left: 50px; top: 86px;
    font-family: "Open Sans", sans-serif;
    font-size: 17px;
    color: var(--text-light);
  }
  .badges {
    position: absolute;
    left: 50px; top: 122px;
    display: flex; gap: 14px; align-items: center;
  }
  .badge-round { width: 34px; height: 34px; border-radius: 50%; background: var(--badge); }
  .badge-square { width: 30px; height: 30px; border-radius: 6px; background: var(--badge); }

  .contact-list {
    position: absolute;
    left: 50px; top: 168px;
    list-style: none;
    font-family: "Open Sans", sans-serif;
    font-size: 13px;
    line-height: 19px;
    color: var(--text-muted);
  }
  .contact-list li { display: flex; align-items: center; gap: 10px; }
  .contact-list svg { width: 12px; height: 12px; fill: var(--accent); flex: none; }
  .contact-list .web-name { color: var(--accent); }

  .address-band {
    position: absolute;
    left: 0; right: 0; bottom: 0;
    height: 38px;
    background: var(--accent);
    display: flex; align-items: center; justify-content: flex-end;
    padding-right: 40px;
    font-family: "Open Sans", sans-serif;
    font-size: 14px;
    color: #ffffff;
  }
</style>
</head>
<body>
<main class="stage">

  <section class="card card-front" aria-label="Card front">
    <div class="front-seal"></div>
    <div class="front-name">SUMMIT GRADING<br>&amp; MASONRY LLC</div>
  </section>

  <section class="card card-back" aria-label="Card back">
    <div class="back-mark">SUMMIT GRADING<br>&amp; MASONRY LLC</div>

    <h1 class="owner-name">MARTIN GALLOWAY</h1>
    <p class="owner-title">Owner</p>

    <div class="badges">
      <span class="badge-round"></span>
      <span class="badge-square"></span>
    </div>

    <ul class="contact-list">
      <li>
        <svg viewBox="0 0 24 24" aria-hidden="true"><path d="M6.6 10.8a15.1 15.1 0 0 0 6.6 6.6l2.2-2.2a1 1 0 0 1 1-.25 11.4 11.4 0 0 0 3.6.57 1 1 0 0 1 1 1V20a1 1 0 0 1-1 1A17 17 0 0 1 3 4a1 1 0 0 1 1-1h3.5a1 1 0 0 1 1 1c0 1.25.2 2.45.57 3.6a1 1 0 0 1-.25 1z"/></svg>
        555 214 3867
      </li>
      <li>
        <svg viewBox="0 0 24 24" aria-hidden="true"><path d="M6 2h9l3 3v5H6z M3 11h18v9H3z M7 14h4v2H7z"/></svg>
        555 630 2719
      </li>
      <li>
        <svg viewBox="0 0 24 24" aria-hidden="true"><path d="M2 5h20v14H2z M3 6l9 7 9-7" stroke="#2d2d2e" stroke-width="1.5"/></svg>
        summitgradingandmasonry@mailbox.example
      </li>
      <li>
        <svg viewBox="0 0 24 24" aria-hidden="true"><path d="M10 2a8 8 0 0 1 6.3 12.9l5.4 5.4-1.4 1.4-5.4-5.4A8 8 0 1 1 10 2zm0 2.5a5.5 5.5 0 1 0 0 11 5.5 5.5 0 0 0 0-11z"/></svg>
        <span>www.<span class="web-name">summitgradingandmasonry</span>.example</span>
      </li>
    </ul>

    <div class="address-band">1840 Ridge Avenue, Millbrook, NY, United States</div>
  </section>

</main>
</body>
</html>
```